Website for Company that serves and supports Investment Banks

We are seeking to have a six page website that provides a basic description of our company's services. Our company provides Financial Models and Investment Memos on an outsourced basis to Small Investment Banks and Investment firms. We do not require a shopping cart. We already have a logo attached.

Target Market(s)

Small, regional investment banks. Small private equity firms.

Industry/Entity Type

Finance And Accounting

Coding

Coded - Design and coding required

Number of Pages Required

5+ page

Requirements
Nice to have
• Please use the logo design to drive how you design the layout for the website

```html
<!DOCTYPE html>
<html lang="en">
<head>
<meta charset="utf-8">
<title>Services | Capstone Deal Analysts</title>
<link href="https://fonts.googleapis.com/css2?family=Montserrat:wght@300;400;500;600;700&display=swap" rel="stylesheet">
<style>
  :root {
    --navy: #0c2747;
    --navy-deep: #081c36;
    --brand-blue: #1b5794;
    --page: #f2f3f5;
    --card: #ffffff;
    --card-border: #d4d8de;
    --ink: #3a3d42;
    --ink-soft: #55595f;
    --rule: #b9bdc3;
    --white: #ffffff;
  }
  * { box-sizing: border-box; margin: 0; padding: 0; }
  html, body { width: 1200px; height: 2604px; overflow: hidden; }
  body {
    background: var(--page);
    font-family: "Montserrat", Arial, sans-serif;
    color: var(--ink);
    position: relative;
  }

  .site-nav {
    position: absolute; left: 0; top: 0; width: 1200px; height: 56px;
    background: var(--navy);
    display: flex; justify-content: space-around; align-items: center;
    padding: 0 40px;
  }
  .site-nav a {
    color: var(--white); text-decoration: none; font-size: 21px; font-weight: 400;
  }
  .site-nav a.is-current { font-weight: 700; }

  .page-title {
    position: absolute; left: 0; top: 96px; width: 1200px;
    display: flex; align-items: center; gap: 36px;
  }
  .page-title::before, .page-title::after {
    content: ""; flex: 1; height: 2px; background: var(--rule);
  }
  .page-title h1 {
    font-size: 60px; font-weight: 300; letter-spacing: 4px; color: var(--ink-soft);
  }

  .section-title {
    position: absolute; left: 0; width: 1200px; text-align: center;
    font-size: 46px; font-weight: 400; letter-spacing: 1px; color: var(--ink);
  }

  .service-card {
    position: absolute;
    background: var(--card);
    border: 2px solid var(--card-border);
    display: flex; flex-direction: column;
  }
  .service-card .card-head {
    background: var(--brand-blue); color: var(--white);
    display: flex; flex-direction: column; align-items: center; justify-content: center;
    text-align: center; font-size: 30px; font-weight: 400; line-height: 1.2;
    padding: 0 12px;
  }
  .service-card .card-head small { font-size: 22px; display: block; margin-top: 4px; }
  .service-card .price {
    flex: 1; display: flex; align-items: center; justify-content: center;
    font-size: 66px; font-weight: 300; color: var(--ink-soft);
  }

  .contact-button {
    position: absolute; left: 432px; top: 2224px; width: 312px; height: 64px;
    background: var(--brand-blue); color: var(--white); text-decoration: none;
    display: flex; align-items: center; justify-content: center;
    font-size: 24px; letter-spacing: 1px;
  }

  .site-footer {
    position: absolute; left: 0; top: 2328px; width: 1200px; height: 240px;
    background: var(--navy);
  }
  .footer-links {
    position: absolute; left: 40px; top: 34px; list-style: none;
  }
  .footer-links li { font-size: 17px; line-height: 26px; color: var(--white); letter-spacing: 0.5px; }
  .footer-contact {
    position: absolute; left: 748px; top: 36px; display: flex; gap: 28px;
    color: var(--white);
  }
  .footer-contact svg { margin-top: 6px; }
  .footer-contact .brand-name { font-size: 19px; font-weight: 700; letter-spacing: 0.5px; }
  .footer-contact p { font-size: 16px; line-height: 24px; }
  .footer-contact .gap { margin-top: 18px; }
  .copyright {
    position: absolute; left: 0; top: 2568px; width: 1200px; height: 36px;
    background: var(--navy-deep); color: var(--white);
    font-size: 15px; letter-spacing: 0.5px;
    display: flex; align-items: center; justify-content: center;
  }
</style>
</head>
<body>

<nav class="site-nav">
  <a href="#">Home</a>
  <a href="#" class="is-current">Services</a>
  <a href="#">Leadership</a>
  <a href="#">Why us?</a>
  <a href="#">Our Process</a>
  <a href="#">Contact Us</a>
</nav>

<div class="page-title"><h1>SERVICES</h1></div>

<h2 class="section-title" style="top:252px">DEAL TRANSACTION MODELS</h2>
<div class="service-card" style="left:20px;top:336px;width:1160px;height:256px">
  <div class="card-head" style="height:80px">LBO, Growth Equity, Recap</div>
  <div class="price">$3,500</div>
</div>

<h2 class="section-title" style="top:668px">VALUATION MODELS</h2>
<div class="service-card" style="left:20px;top:768px;width:372px;height:244px">
  <div class="card-head" style="height:124px">Discounted<br>Cashflows</div>
  <div class="price">$2,500</div>
</div>
<div class="service-card" style="left:414px;top:768px;width:372px;height:244px">
  <div class="card-head" style="height:124px">Comparable<br>Company Analysis</div>
  <div class="price">$1,000</div>
</div>
<div class="service-card" style="left:808px;top:768px;width:372px;height:244px">
  <div class="card-head" style="height:124px">Private Multiple<br>Analysis</div>
  <div class="price">$1,000</div>
</div>

<h2 class="section-title" style="top:1108px">INVESTMENT MEMOS</h2>
<div class="service-card" style="left:20px;top:1192px;width:372px;height:260px">
  <div class="card-head" style="height:128px">Investment Memo<small>15-20 pages</small></div>
  <div class="price">$3,500</div>
</div>
<div class="service-card" style="left:414px;top:1192px;width:372px;height:260px">
  <div class="card-head" style="height:128px">Investor Slide Deck<small>15-20 pages</small></div>
  <div class="price">$3,500</div>
</div>
<div class="service-card" style="left:808px;top:1192px;width:372px;height:260px">
  <div class="card-head" style="height:128px">CIM<small>40-50 pages</small></div>
  <div class="price">$6,500</div>
</div>

<h2 class="section-title" style="top:1532px">DEAL SUPPORT MEMOS</h2>
<div class="service-card" style="left:20px;top:1620px;width:568px;height:240px">
  <div class="card-head" style="height:120px">Executive Summary Teaser<small>2 pages</small></div>
  <div class="price">$500</div>
</div>
<div class="service-card" style="left:612px;top:1620px;width:568px;height:240px">
  <div class="card-head" style="height:120px">Investment Screening Memo<small>2 pages</small></div>
  <div class="price">$500</div>
</div>
<div class="service-card" style="left:20px;top:1904px;width:568px;height:240px">
  <div class="card-head" style="height:120px">Customized Industry<br>Research</div>
  <div class="price">$500</div>
</div>
<div class="service-card" style="left:612px;top:1904px;width:568px;height:240px">
  <div class="card-head" style="height:120px">Customized Company<br>Research</div>
  <div class="price">$500</div>
</div>

<a href="#" class="contact-button">CONTACT US</a>

<footer class="site-footer">
  <ul class="footer-links">
    <li>HOME</li>
    <li>SERVICES</li>
    <li>LEADERSHIP</li>
    <li>WHY US?</li>
    <li>OUR PROCESS</li>
    <li>CONTACT US</li>
  </ul>
  <div class="footer-contact">
    <svg width="34" height="48" viewBox="0 0 34 48" aria-hidden="true">
      <path d="M17 0C7.6 0 0 7.6 0 17c0 12.8 17 31 17 31s17-18.2 17-31C34 7.6 26.4 0 17 0z" fill="#ffffff"/>
      <circle cx="17" cy="17" r="6.5" fill="#0c2747"/>
    </svg>
    <div>
      <div class="brand-name">CAPSTONEDEALANALYSTS.COM</div>
      <p>410 Harbor Street</p>
      <p>Suite 12-204</p>
      <p>Portland, ME 04101</p>
      <p class="gap">Phone: 207-555-0148</p>
      <p>Email: info@capstonedealanalysts.com</p>
    </div>
  </div>
</footer>
<div class="copyright">© CAPSTONEDEALANALYSTS.COM 2018. ALL RIGHTS RESERVED.</div>

</body>
</html>
```